Business card design only (Have Logo Online) Shoudl be quick and easy for designer

We would like to have a business card design that is in-line with our company logo. Final deliverables should include two EPS extension file. One for the front card design and the other the back-end design. Please also indicate the font style used.

Advisory Pebble is a social enterprise that focuses on utilizing technology, unique methodologies and international partnerships to provide a one-stop location for economical and dependable IT-related solutions.

Target Market(s)

Micro, small and medium business owners.

Industry/Entity Type

Business

Requirements
Must have
• The business card should incorporate our company logo.
Nice to have
• A little web 2.0 style would be nice but I haven''t decided yet.

```html
<!DOCTYPE html>
<html lang="en">
<head>
<meta charset="utf-8">
<title>Advisory Pebble – Business Card</title>
<link rel="stylesheet" href="https://fonts.googleapis.com/css2?family=Arimo:ital,wght@0,700;1,400&family=Source+Sans+3:wght@400;700&display=swap">
<style>
  :root {
    --page: #ffffff;
    --card: #f0fce5;
    --band: #ccfe9c;
    --mat: #f7faf5;
    --green: #4cb034;
    --leaf-soft: #b2e6a0;
    --lime-soft: #d9fcb8;
    --lime: #bff98a;
    --ink: #1b1f1a;
    --edge: #4a4f4a;
  }
  * { margin: 0; padding: 0; box-sizing: border-box; }
  html, body { width: 927px; height: 1200px; overflow: hidden; background: var(--page); }
  .sheet { position: relative; width: 927px; height: 1200px; }
  .card {
    position: absolute; left: 50px; width: 364px; height: 208px;
    background: var(--card); border: 1px solid var(--edge); overflow: hidden;
  }
  .card--front { top: 50px; }
  .front-art {
    position: absolute; left: -40px; top: -10px; width: 235px; height: 240px;
    border-radius: 0 50% 50% 0;
    background:
      radial-gradient(ellipse 60% 55% at 45% 35%, var(--leaf-soft) 0%, rgba(178,230,160,0.55) 55%, rgba(178,230,160,0) 100%),
      radial-gradient(ellipse 70% 70% at 60% 60%, var(--lime-soft) 0%, rgba(217,252,184,0) 100%);
  }
  .back-mat { position: absolute; left: 44px; top: 299px; width: 375px; height: 220px; background: var(--mat); }
  .card--back { top: 306px; }
  .contact {
    position: absolute; right: 15px; top: 14px; text-align: right;
    font-family: "Source Sans 3", "Myriad Pro", sans-serif; color: var(--ink);
  }
  .contact__name { font-family: Arimo, Arial, sans-serif; font-weight: 700; font-size: 21px; color: var(--green); line-height: 1.1; }
  .contact__role { font-family: Arimo, Arial, sans-serif; font-style: italic; font-size: 12px; margin-right: 47px; line-height: 1.2; }
  .contact__address { margin-top: 16px; font-size: 15.5px; line-height: 19px; }
  .contact__lines { margin-top: 15px; font-size: 14px; line-height: 17.5px; margin-right: -1px; }
  .band { position: absolute; left: 230px; top: 0; width: 134px; height: 100%; background: var(--band); }
  .back-art {
    position: absolute; left: 14px; top: 22px; width: 172px; height: 172px; border-radius: 50%;
    background: radial-gradient(circle at 50% 42%, rgba(191,249,138,0) 0%, rgba(191,249,138,0.35) 60%, var(--lime) 100%);
  }
  .brand {
    position: absolute; left: 50px; top: 119px;
    display: flex; align-items: center; gap: 8px;
  }
  .brand__dot { width: 22px; height: 22px; border-radius: 50%; background: var(--green); }
  .brand__name {
    font-family: "Source Sans 3", "Myriad Pro", sans-serif; font-weight: 700;
    font-size: 36px; line-height: 1; color: var(--green); letter-spacing: 0.3px;
  }
</style>
</head>
<body>
<div class="sheet">
  <section class="card card--front">
    <div class="front-art" role="img" aria-label="Faint green brand illustration"></div>
    <div class="contact">
      <div class="contact__name">Rowan Tessier</div>
      <div class="contact__role">Founder</div>
      <div class="contact__address">1420 Alder Lane<br>BC Canada<br>V6K 2M1</div>
      <div class="contact__lines">Cell: 1-604-555-0148<br>E-mail: rowan.tessier@advisorypebble.com<br>www.advisorypebble.com</div>
    </div>
  </section>

  <div class="back-mat"></div>
  <section class="card card--back">
    <div class="band"></div>
    <div class="back-art" role="img" aria-label="Soft green brand illustration"></div>
    <div class="brand">
      <span class="brand__dot"></span>
      <span class="brand__name">Advisory Pebble</span>
    </div>
  </section>
</div>
</body>
</html>
```